New concept for existing event brand

I have this current brand - www.velltrix-quarter.com I have attached an example of a credible event on 23rd December and then a more fun brunch event.

I require a new flyer for a new concept - Fernwick Frolics - (there is no logo yet) it is at a venue which has ball pits, table tennis, beer pong, arcades etc

I am looking for an artwork which portrays a fun event but also retains the cooler brand identify

One idea was having the images in polaroid frames

Fernwick Frolics

Saturday 18th February 2023

Venue to be announced • 3pm-9pm

2 giant ball pits
Beer pong
Ping Pong
Boxing machines
Dance Machine
Air Hockey
Pool
Giant board games
Giant Stackle 6
Photo Booth
Spin The Wheel
Table Football
Retro Arcade Games
Pinball

Food
Pizzas
Brimsy Bowls
Popcorn
Candy Floss

Cocktails
Alcoholic Chillo Kittens
Beer Towers
Spirits & Mixers

```html
<!DOCTYPE html>
<html lang="en">
<head>
<meta charset="utf-8">
<title>Fernwick Frolics – Saturday 18th February 2023</title>
<link href="https://fonts.googleapis.com/css2?family=Bebas+Neue&family=Oswald:wght@300;400;500&display=swap" rel="stylesheet">
<style>
  :root {
    --purple-bright: #b41ad6;
    --purple-mid: #7a10a8;
    --purple-deep: #3e0560;
    --purple-night: #2a0340;
    --white: #ffffff;
    --pink-accent: #f08ad8;
    --pill-cyan: #27c3ec;
    --pill-blue: #2a7fe0;
    --tape: rgba(235, 228, 240, 0.72);
    --photo-frame: #f7f5f7;
  }
  * { margin: 0; padding: 0; box-sizing: border-box; }
  html, body { width: 1192px; height: 1200px; overflow: hidden; background: var(--purple-night); }
  .flyer {
    position: relative;
    width: 1192px;
    height: 1200px;
    overflow: hidden;
    background: linear-gradient(160deg, var(--purple-bright) 0%, var(--purple-mid) 30%, var(--purple-deep) 60%, var(--purple-night) 100%);
    font-family: 'Oswald', sans-serif;
    color: var(--white);
  }
  .ball-pit-backdrop {
    position: absolute;
    left: 0; right: 0; bottom: 0;
    height: 520px;
    background:
      radial-gradient(ellipse at 20% 70%, rgba(200,111,196,0.55), transparent 55%),
      radial-gradient(ellipse at 80% 80%, rgba(180,90,200,0.5), transparent 55%),
      linear-gradient(180deg, transparent 0%, rgba(150,60,170,0.55) 45%, rgba(110,40,140,0.75) 100%);
  }
  .event-title {
    position: absolute;
    left: 58px; top: 66px;
    font-family: 'Bebas Neue', sans-serif;
    font-weight: 400;
    font-size: 84px;
    line-height: 0.95;
    letter-spacing: 1px;
  }
  .site-url {
    position: absolute;
    right: 62px; top: 70px;
    font-weight: 400;
    font-size: 25px;
    letter-spacing: 2.5px;
    text-transform: uppercase;
  }
  .polaroid {
    position: absolute;
    background: var(--photo-frame);
    padding: 22px;
    box-shadow: 0 10px 26px rgba(0,0,0,0.45);
  }
  .polaroid .photo { width: 100%; height: 100%; }
  .polaroid--ball-pit { left: 352px; top: 100px; width: 476px; height: 476px; transform: rotate(3deg); }
  .polaroid--ball-pit .photo { background: radial-gradient(circle at 50% 40%, #c9c3cc, #8e8794 70%, #6b6471); }
  .polaroid--arcade { left: 201px; top: 430px; width: 337px; height: 352px; transform: rotate(-5deg); }
  .polaroid--arcade .photo { background: linear-gradient(160deg, #3a4f6b, #7a5a6e 50%, #2b2a3e); }
  .polaroid--beer-pong { left: 565px; top: 389px; width: 377px; height: 420px; transform: rotate(4deg); }
  .polaroid--beer-pong .photo { background: linear-gradient(170deg, #2a2f45, #5a3c55 50%, #8a3a44); }
  .tape { position: absolute; background: var(--tape); }
  .tape--ball-pit { left: 585px; top: 50px; width: 66px; height: 124px; transform: rotate(22deg); }
  .tape--arcade { left: 318px; top: 380px; width: 58px; height: 118px; transform: rotate(-16deg); }
  .tape--beer-pong { left: 735px; top: 345px; width: 58px; height: 118px; transform: rotate(-14deg); }
  .event-date {
    position: absolute;
    left: 0; right: 0; top: 826px;
    text-align: center;
    font-family: 'Bebas Neue', sans-serif;
    font-weight: 400;
    font-size: 52px;
    letter-spacing: 0.5px;
  }
  .event-venue-time {
    position: absolute;
    left: 0; right: 0; top: 880px;
    text-align: center;
    font-weight: 300;
    font-size: 32px;
    color: rgba(255,255,255,0.85);
    text-transform: uppercase;
  }
  .activities {
    position: absolute;
    left: 83px; top: 938px;
    width: 1026px; height: 112px;
    border-radius: 22px;
    border: 2px solid rgba(255,255,255,0.35);
    background: linear-gradient(90deg, var(--pill-cyan), var(--pill-blue));
    display: flex; flex-direction: column; justify-content: center; align-items: center;
    font-weight: 300;
    font-size: 21px;
    line-height: 1.6;
    text-transform: uppercase;
  }
  .activities strong { font-weight: 500; }
  .menu {
    position: absolute;
    left: 0; right: 0; top: 1070px;
    text-align: center;
    font-weight: 300;
    font-size: 18px;
    line-height: 1.6;
    letter-spacing: 1.5px;
    text-transform: uppercase;
  }
  .menu .accent { color: var(--pink-accent); }
</style>
</head>
<body>
  <main class="flyer">
    <div class="ball-pit-backdrop" role="img" aria-label="Blurred ball pit balls in pink and purple"></div>

    <h1 class="event-title">Fernwick<br>Frolics</h1>
    <div class="site-url">www.velltrix-quarter.com</div>

    <figure class="polaroid polaroid--ball-pit">
      <div class="photo" role="img" aria-label="Photo of a guest playing in a ball pit of white and grey balls"></div>
    </figure>
    <figure class="polaroid polaroid--arcade">
      <div class="photo" role="img" aria-label="Photo of two guests on an arcade dance machine"></div>
    </figure>
    <figure class="polaroid polaroid--beer-pong">
      <div class="photo" role="img" aria-label="Photo of a group of friends playing beer pong"></div>
    </figure>

    <span class="tape tape--ball-pit"></span>
    <span class="tape tape--arcade"></span>
    <span class="tape tape--beer-pong"></span>

    <h2 class="event-date">Saturday 18th February 2023</h2>
    <p class="event-venue-time">Venue to be announced • 3pm-9pm</p>

    <section class="activities">
      <p>2 giant ball pits, <strong>beer pong</strong>, ping pong, <strong>boxing machines</strong>, dance machine, <strong>air hockey</strong>, pool</p>
      <p><strong>giant board games</strong>, giant Stackle 6, <strong>photo booth</strong>, spin the wheel, <strong>table football</strong>, retro arcade games, <strong>pinball</strong></p>
    </section>

    <section class="menu">
      <p>Food, <span class="accent">Pizzas</span>, Brimsy Bowls, <span class="accent">Popcorn</span>, Candy Floss</p>
      <p><span class="accent">Cocktails</span>, Alcoholic Chillo Kittens, <span class="accent">Beer Towers</span>, Spirits &amp; Mixers</p>
    </section>
  </main>
</body>
</html>
```